Stationary for ultrasound imaging company
Business card, letter head, statonary envelope, fax cover sheet
Silver-Fern
Lino Varsek
Account Executive
20947 Marlow Pine Lane
Alderwick, OR 97215
linovarsek@postmeadow.com
at www.brisolavent.com
This is the logo for the company.

```html
<!DOCTYPE html>
<html lang="en">
<head>
<meta charset="utf-8">
<title>Silver-Fern Business Card</title>
<link href="https://fonts.googleapis.com/css2?family=Open+Sans:wght@400;600;700&display=swap" rel="stylesheet">
<style>
  :root {
    --brand-blue: #2aa6e0;
    --deep-blue: #1f86c4;
    --ink-grey: #4a4a4a;
    --band-grey: #a9abae;
    --card-white: #ffffff;
    --stage: #e6e7e9;
  }
  * { margin: 0; padding: 0; box-sizing: border-box; }
  html, body { width: 1200px; height: 902px; overflow: hidden; background: var(--stage); }
  body { font-family: "Open Sans", Arial, sans-serif; position: relative; }

  .business-card {
    position: absolute; left: 100px; top: 165px;
    width: 1000px; height: 572px;
    background: var(--card-white);
    box-shadow: 0 10px 30px rgba(0,0,0,0.18);
    overflow: hidden;
  }
  .brand { position: absolute; left: 190px; top: 60px; display: flex; align-items: center; gap: 20px; }
  .brand-mark { width: 80px; height: 80px; background: var(--brand-blue); }
  .brand-name { font-size: 76px; font-weight: 700; color: var(--deep-blue); letter-spacing: -2px; line-height: 1; }

  .holder { position: absolute; left: 380px; top: 228px; }
  .holder-name { font-size: 30px; font-weight: 600; color: var(--brand-blue); line-height: 1.2; }
  .holder-title { font-size: 22px; color: var(--ink-grey); margin-top: 6px; }

  .contact { position: absolute; left: 60px; top: 364px; right: 30px; font-size: 18px; color: var(--ink-grey); }
  .contact-row { display: flex; gap: 24px; margin-bottom: 12px; white-space: nowrap; }
  .contact-item { display: flex; align-items: center; gap: 8px; }
  .contact-icon { width: 22px; height: 22px; flex: none; }

  .band-grey { position: absolute; top: 468px; height: 28px; background: var(--band-grey); }
  .band-grey.left { left: 0; width: 340px; }
  .band-grey.right { right: 0; width: 120px; }
  .band-web {
    position: absolute; left: 340px; top: 468px; width: 540px; height: 52px;
    background: var(--brand-blue); color: #fff;
    font-size: 22px; letter-spacing: 4px;
    display: flex; align-items: center; justify-content: center;
  }
</style>
</head>
<body>
  <div class="business-card">
    <div class="brand">
      <div class="brand-mark"></div>
      <div class="brand-name">Silver-Fern</div>
    </div>

    <div class="holder">
      <div class="holder-name">Lino Varsek</div>
      <div class="holder-title">Account Executive</div>
    </div>

    <div class="contact">
      <div class="contact-row">
        <span class="contact-item">
          <svg class="contact-icon" viewBox="0 0 22 22"><circle cx="11" cy="11" r="11" fill="#2aa6e0"/><path d="M11 5 5 10.5h2V16h8v-5.5h2z" fill="#fff"/></svg>
          20947 Marlow Pine Lane Alderwick, OR 97215
        </span>
        <span class="contact-item">
          <svg class="contact-icon" viewBox="0 0 22 22"><circle cx="11" cy="11" r="11" fill="#2aa6e0"/><path d="M7 6c1-1 2 0 3 2s-1 2 0 3 2 3 3 2 1-1 2 0 1 2 0 3c-3 2-10-5-8-10z" fill="#fff"/></svg>
          713-404-2817
        </span>
        <span class="contact-item">
          <svg class="contact-icon" viewBox="0 0 22 22"><circle cx="11" cy="11" r="11" fill="#2aa6e0"/><rect x="8" y="5" width="6" height="12" rx="1" fill="#fff"/></svg>
          314-602-7731
        </span>
      </div>
      <div class="contact-row">
        <span class="contact-item">
          <svg class="contact-icon" viewBox="0 0 22 22"><circle cx="11" cy="11" r="11" fill="#2aa6e0"/><rect x="6" y="8" width="10" height="8" fill="#fff"/><rect x="8" y="5" width="6" height="3" fill="#fff"/></svg>
          123-555-01472
        </span>
        <span class="contact-item">
          <svg class="contact-icon" viewBox="0 0 22 22"><circle cx="11" cy="11" r="11" fill="#2aa6e0"/><rect x="5" y="7" width="12" height="8" fill="#fff"/><path d="M5 7l6 5 6-5" stroke="#2aa6e0" stroke-width="1.2" fill="none"/></svg>
          linovarsek@postmeadow.com
        </span>
        <span class="contact-item">
          <svg class="contact-icon" viewBox="0 0 22 22"><circle cx="11" cy="11" r="11" fill="#2aa6e0"/><circle cx="11" cy="11" r="6" fill="none" stroke="#fff" stroke-width="1.5"/><path d="M5 11h12M11 5v12" stroke="#fff" stroke-width="1.2"/></svg>
          www.brisolavent.com
        </span>
      </div>
    </div>

    <div class="band-grey left"></div>
    <div class="band-grey right"></div>
    <div class="band-web">www.brisolavent.com</div>
  </div>
</body>
</html>
```